Welcome Center Signage/logo Design with Multicultural Relevance

We are looking to have a welcome signage/logo designed for our church lobby with either the word "welcome" or "Welcome to the Maplecrest Fellowship Church!"

This design must include our organizational logo (attached). It could (but does not need to) also include our church vision: "Our vision is to be a thriving diverse urban church sharing Christ's love and serving the needs of our local and global communities." The logo/signage will be printed on 4' x 6' stretch fabric.

This signage will then be hung up behind our welcome center...it will be one of the first things people see upon entering our building.

We are an urban multicultural church that has significant outreach into our local community, one that is quite culturally diverse. If you would like more information about our church, please visit www.maplecrestfellow.org.
Updates

Project Deadline Extended
Reason: We have committed to continue work with the designers on designs submitted over the last several days, and are scheduling the additional time needed to do so. Thank you!

Target Market(s)

Culturally (African American, Hispanic American, Asian American, European American) diverse millennials and iGens

Industry/Entity Type

Church

Font styles to use
Sans Serif

Requirements
Must have
• Our logo
Nice to have
• "Welcome" in many languages
Should not have
• I can't think of anything at the moment.

```html
<!DOCTYPE html>
<html lang="en">
<head>
<meta charset="utf-8">
<title>Welcome Sign – Maplecrest Fellowship Church</title>
<link rel="stylesheet" href="https://fonts.googleapis.com/css2?family=Exo+2:wght@600;700;800&display=swap">
<style>
  :root {
    --page: #e4e4e4;
    --fabric: #ddd7c9;
    --gold: #d3910f;
    --gold-fold: #b37808;
    --navy: #4b4a69;
    --slate: #5f5d7d;
    --rose: #9d5e5a;
    --plum: #7c5669;
    --mauve: #8c5d7b;
    --brick: #8d4d53;
    --fold-shade: rgba(0,0,0,0.18);
    --label: #e6ddd0;
    --ink: #141414;
    --seal: #6a2f33;
    --seal-ring: #b8262b;
  }
  html, body {
    margin: 0;
    width: 1200px;
    height: 900px;
    overflow: hidden;
    background: var(--page);
  }
  .sign {
    position: absolute;
    left: 30px;
    top: 70px;
    width: 1140px;
    height: 760px;
    display: block;
  }
  .sign-text {
    font-family: "Exo 2", sans-serif;
    font-weight: 700;
  }
  .ribbon-label {
    fill: var(--label);
    font-size: 26px;
    letter-spacing: 3px;
    text-anchor: middle;
  }
  .welcome-label {
    fill: var(--label);
    font-size: 42px;
    font-weight: 800;
    letter-spacing: 8px;
    text-anchor: middle;
  }
  .church-name {
    fill: var(--label);
    font-size: 30px;
    letter-spacing: 2px;
    text-anchor: middle;
  }
  .vision {
    fill: var(--ink);
    font-size: 14.5px;
    letter-spacing: 2.2px;
    text-anchor: middle;
  }
</style>
</head>
<body>
<svg class="sign sign-text" viewBox="0 0 960 640" xmlns="http://www.w3.org/2000/svg">
  <rect class="fabric" width="960" height="640" fill="var(--fabric)"/>

  <!-- main welcome ribbon -->
  <g class="ribbon ribbon-welcome">
    <polygon points="322,55 322,3 345,20 430,22 430,55" fill="var(--gold-fold)"/>
    <polygon points="540,130 640,130 640,165 620,192 620,152 540,152" fill="var(--gold-fold)"/>
    <rect x="298" y="55" width="370" height="75" fill="var(--gold)"/>
    <text class="welcome-label" x="483" y="107">WELCOME</text>
  </g>

  <!-- language ribbons, left -->
  <g class="ribbon ribbon-welkom" transform="translate(175 200) rotate(12)">
    <polygon points="70,30 118,30 92,64" fill="var(--navy)"/>
    <rect x="-135" y="-30" width="270" height="60" fill="var(--navy)"/>
    <text class="ribbon-label" x="-15" y="9">WELKOM</text>
  </g>
  <g class="ribbon ribbon-bem-vinda" transform="translate(145 358)">
    <polygon points="82,28 115,28 106,62" fill="var(--rose)"/>
    <rect x="-135" y="-28" width="270" height="56" fill="var(--rose)"/>
    <text class="ribbon-label" x="-10" y="9">BEM VINDA</text>
  </g>
  <g class="ribbon ribbon-benvinguda" transform="translate(160 520) rotate(-12)">
    <polygon points="70,30 118,30 102,66" fill="var(--mauve)"/>
    <rect x="-135" y="-30" width="270" height="60" fill="var(--mauve)"/>
    <text class="ribbon-label" x="-10" y="9">BENVINGUDA</text>
  </g>

  <!-- language ribbons, right -->
  <g class="ribbon ribbon-bienvenue" transform="translate(800 205) rotate(-12)">
    <polygon points="-135,-30 -120,-54 -70,-54 -70,-30" fill="var(--slate)"/>
    <polygon points="-135,-30 -120,-54 -70,-54 -70,-30" fill="var(--fold-shade)"/>
    <rect x="-135" y="-30" width="270" height="60" fill="var(--slate)"/>
    <text class="ribbon-label" x="10" y="9">BIENVENUE</text>
  </g>
  <g class="ribbon ribbon-bienvenido" transform="translate(812 368)">
    <polygon points="-127,-31 -112,-62 -80,-62 -80,-31" fill="var(--plum)"/>
    <polygon points="-127,-31 -112,-62 -80,-62 -80,-31" fill="var(--fold-shade)"/>
    <rect x="-127" y="-31" width="255" height="62" fill="var(--plum)"/>
    <text class="ribbon-label" x="0" y="9">BIENVENIDO</text>
  </g>
  <g class="ribbon ribbon-willkommen" transform="translate(785 522) rotate(12)">
    <polygon points="-140,-31 -125,-62 -85,-62 -85,-31" fill="var(--brick)"/>
    <polygon points="-140,-31 -125,-62 -85,-62 -85,-31" fill="var(--fold-shade)"/>
    <rect x="-140" y="-31" width="280" height="62" fill="var(--brick)"/>
    <text class="ribbon-label" x="5" y="9">WILLKOMMEN</text>
  </g>

  <!-- church name in the seal position -->
  <g class="church-seal">
    <circle cx="480" cy="360" r="182" fill="var(--seal)" stroke="var(--seal-ring)" stroke-width="6"/>
    <text class="church-name" x="480" y="335">MAPLECREST</text>
    <text class="church-name" x="480" y="372">FELLOWSHIP</text>
    <text class="church-name" x="480" y="409">CHURCH</text>
  </g>

  <!-- vision statement -->
  <g class="vision-statement">
    <text class="vision" x="480" y="584">OUR VISION IS TO BE A THRIVING DIVERSE URBAN CHURCH</text>
    <text class="vision" x="480" y="605">SHARING CHRIST'S LOVE AND SERVING THE NEEDS</text>
    <text class="vision" x="480" y="626">OF OUR LOCAL AND GLOBAL COMMUNITIES</text>
  </g>
</svg>
</body>
</html>
```